Lantern Advisory Website

I currently have a website www.lanternadvisoryinc.example. We are a IT Consulting Company. Our website will pretty much tell out our services. I am looking to enhance my website and make it look more professional. Looking for very classy and Contemporary look and design for my website.

It Company

```html
<!DOCTYPE html>
<html lang="en">
<head>
<meta charset="utf-8">
<title>Lantern Advisory</title>
<link href="https://fonts.googleapis.com/css2?family=Arimo:wght@400;700&family=Open+Sans:ital,wght@0,400;0,600;1,400&family=Raleway:wght@400;500;600&display=swap" rel="stylesheet">
<style>
:root{
  --navy:#0d3a7d;
  --heading:#1b3f8c;
  --sky:#0a9ad6;
  --ink:#111;
  --grey:#555;
  --light:#f4f6f8;
  --white:#fff;
  --dark:#1d2126;
  --black:#000;
}
*{margin:0;padding:0;box-sizing:border-box}
html,body{width:1200px;height:3636px;overflow:hidden}
body{position:relative;background:var(--white);font-family:"Open Sans",sans-serif;color:var(--ink)}
.abs{position:absolute}
.center{left:0;width:1200px;text-align:center}

/* header */
.site-header{top:0;left:0;width:1200px;height:95px;background:var(--white)}
.brand{display:flex;align-items:center;gap:12px;font-family:"Raleway",sans-serif;font-weight:600;font-size:24px;color:var(--navy)}
.brand .mark{width:30px;height:30px;background:var(--navy)}
.site-header .brand{left:82px;top:30px}
.main-nav{right:82px;top:34px;display:flex;gap:22px;font-family:"Raleway",sans-serif;font-size:17px;color:#333}
.main-nav .active{color:var(--sky);border-bottom:2px solid var(--sky);padding-bottom:6px}

/* hero */
.hero{top:95px;left:0;width:1200px;height:707px;background:linear-gradient(100deg,#c9d6df 0%,#eef2f4 35%,#dfe4e7 60%,#6f7b86 100%)}
.hero-title{top:262px;font-family:"Arimo",sans-serif;font-size:54px;line-height:62px;color:var(--heading)}
.btn-solid{background:var(--navy);color:var(--white);font-family:"Raleway",sans-serif;display:flex;align-items:center;justify-content:center}
.hero-btn{left:500px;top:412px;width:198px;height:48px;font-size:20px}
.dots{top:646px;left:572px;display:flex;gap:14px}
.dots span{width:10px;height:10px;border-radius:50%;background:rgba(255,255,255,.6)}
.dots span.on{background:var(--white)}

/* welcome */
.welcome-title{top:890px;font-family:"Arimo",sans-serif;font-size:42px;color:var(--ink)}
.welcome-title em{font-style:normal;color:var(--navy)}
.welcome-rule{left:528px;top:948px;width:452px;height:3px;background:var(--navy)}
.welcome-text{left:145px;top:988px;width:922px;text-align:center;font-size:15px;line-height:27px;color:var(--grey)}
.btn-outline{border:2px solid #333;font-family:"Raleway",sans-serif;font-size:16px;display:flex;align-items:center;justify-content:center}
.read-more{left:536px;top:1100px;width:128px;height:40px;color:var(--ink)}

/* services */
.services{top:1224px;left:0;width:1200px;height:657px;background:linear-gradient(100deg,#2c2a26 0%,#4a4a44 40%,#3b3f45 70%,#2a2d33 100%)}
.services-diamond{left:437px;top:1364px;width:326px;height:326px;transform:rotate(45deg);background:linear-gradient(135deg,#4d7fc9,#1f4f9c)}
.diamond-name{top:1455px;font-family:"Raleway",sans-serif;font-weight:600;font-size:22px;color:var(--white)}
.diamond-title{top:1510px;font-family:"Arimo",sans-serif;font-size:44px;color:var(--white)}
.svc-label{font-family:"Raleway",sans-serif;font-size:21px;line-height:27px;color:var(--white)}
.svc-icon{width:54px;height:54px}
.services-more{left:558px;top:1777px;width:84px;height:38px;border-color:var(--white);color:var(--white);font-size:15px}

/* vision */
.vision-title{left:184px;top:2018px;font-family:"Arimo",sans-serif;font-size:38px;line-height:52px;color:var(--navy)}
.vision-rule{left:184px;top:2130px;width:58px;height:3px;background:var(--navy)}
.vision-text{left:184px;top:2160px;width:400px;font-style:italic;font-size:13.5px;line-height:24px;color:var(--grey)}
.photo-back{left:768px;top:1963px;width:250px;height:316px;background:linear-gradient(160deg,#2b3340,#4a5563)}
.photo-front{left:635px;top:2017px;width:250px;height:310px;background:linear-gradient(180deg,#cfd3d6,#8d939a)}
.photo-front::after{content:"";position:absolute;left:10px;top:10px;right:10px;bottom:10px;border:2px solid var(--white)}

/* clients */
.clients-title{top:2416px;font-family:"Arimo",sans-serif;font-size:38px;color:var(--navy)}
.clients-rule{left:570px;top:2472px;width:60px;height:3px;background:var(--navy)}
.quote-mark{left:580px;top:2499px;width:40px;height:40px}
.clients-text{top:2560px;font-size:15px;line-height:26px;color:var(--grey)}
.by{top:2627px;font-size:14px;color:var(--grey)}
.client-name{top:2655px;font-size:15px;font-weight:600;color:var(--ink)}
.avatar{left:565px;top:2692px;width:70px;height:70px;border-radius:50%;background:linear-gradient(135deg,#a57e6d,#5c4037)}

/* consulting band */
.consult{top:2831px;left:0;width:1200px;height:335px;background:linear-gradient(100deg,#2e3238 0%,#555b62 55%,#3a3f45 100%)}
.consult-title{left:99px;top:2890px;font-family:"Arimo",sans-serif;font-size:30px;color:var(--white)}
.consult-sub{left:99px;top:2940px;font-size:15px;color:var(--white)}
.start-btn{left:831px;top:2913px;width:199px;height:47px;font-size:20px}

/* footer base + newsletter */
.footer-bg{top:3166px;left:0;width:1200px;height:470px;background:var(--black)}
.newsletter{left:78px;top:3020px;width:1044px;height:264px;background:var(--sky)}
.news-title{top:3072px;font-family:"Arimo",sans-serif;font-size:33px;color:var(--white)}
.field{top:3163px;width:219px;height:44px;border:2px solid var(--white);color:var(--white);font-size:15px;padding:10px 8px}
.subscribe{left:727px;top:3163px;width:175px;height:44px;font-size:20px}

.site-footer .brand{left:85px;top:3414px;color:var(--white);font-size:22px}
.site-footer .brand .mark{background:var(--sky)}
.foot-head{top:3342px;font-size:17px;color:var(--white)}
.foot-line{font-size:12.5px;color:var(--white);line-height:22px}
.foot-links{left:703px;top:3380px;font-family:"Raleway",sans-serif;font-size:13px;line-height:28.5px;color:var(--white)}
.foot-icon{width:16px;height:16px}
.social-dot{width:14px;height:14px;border-radius:50%;background:var(--white)}
.copyright{top:3573px;font-size:14px;color:var(--white)}
.copyright b{font-weight:600}
</style>
</head>
<body>

<header class="site-header abs">
  <div class="brand abs"><span class="mark"></span>Lantern Advisory</div>
  <nav class="main-nav abs">
    <span class="active">COMPANY</span><span>SERVICES</span><span>SOLUTION</span><span>RESOURCES</span><span>CAREER</span><span>CONTACT US</span>
  </nav>
</header>

<section class="hero abs" role="img" aria-label="Smiling business team working together at a computer in a bright office"></section>
<h1 class="hero-title abs center">STEADY GROWTH, FOR YOUR<br>OWN&nbsp; !</h1>
<div class="hero-btn btn-solid abs">Contact Us</div>
<div class="dots abs"><span class="on"></span><span></span><span></span></div>

<h2 class="welcome-title abs center">WELCOME TO <em>LANTERN ADVISORY</em></h2>
<div class="welcome-rule abs"></div>
<p class="welcome-text abs">Delivers highest level of Quality Consultants and services for the lowest Cost of Ownership. Forge Client relationships to better understand and respond to their business needs.Forge Client relationships to better understand and respond to their business needs.Develop, challenge, empower and recognize our employees .</p>
<div class="read-more btn-outline abs">Read More</div>

<section class="services abs" role="img" aria-label="Two colleagues discussing work in a dimly lit office"></section>
<div class="services-diamond abs" role="img" aria-label="Hand reaching toward a screen"></div>
<div class="diamond-name abs center">Lantern Advisory</div>
<div class="diamond-title abs center">SERVICES</div>

<div class="svc-label abs" style="left:126px;top:1415px">TECHNOLOGY</div>
<svg class="svc-icon abs" style="left:300px;top:1398px" viewBox="0 0 54 54"><rect x="11" y="11" width="32" height="32" transform="rotate(45 27 27)" fill="#0d3a7d"/><rect x="22" y="17" width="10" height="19" rx="2" fill="none" stroke="#fff" stroke-width="2"/><circle cx="27" cy="33" r="1.2" fill="#fff"/></svg>

<div class="svc-label abs" style="left:126px;top:1556px">APPLICATON<br>DEVLOPMENT</div>
<svg class="svc-icon abs" style="left:303px;top:1553px" viewBox="0 0 54 54"><rect x="11" y="11" width="32" height="32" transform="rotate(45 27 27)" fill="#0d3a7d"/><rect x="20" y="21" width="14" height="13" rx="2" fill="#fff"/><rect x="23" y="34" width="2.5" height="4" fill="#fff"/><rect x="28.5" y="34" width="2.5" height="4" fill="#fff"/></svg>

<div class="svc-label abs" style="left:924px;top:1405px">OFFSHORE</div>
<svg class="svc-icon abs" style="left:833px;top:1393px" viewBox="0 0 54 54"><rect x="11" y="11" width="32" height="32" transform="rotate(45 27 27)" fill="#0d3a7d"/><circle cx="27" cy="22" r="4" fill="#fff"/><path d="M20 35c0-5 3-8 7-8s7 3 7 8z" fill="#fff"/></svg>

<div class="svc-label abs" style="left:921px;top:1558px">ENTERPRISE<br>INTEGRATION</div>
<svg class="svc-icon abs" style="left:838px;top:1553px" viewBox="0 0 54 54"><rect x="11" y="11" width="32" height="32" transform="rotate(45 27 27)" fill="#0d3a7d"/><rect x="19" y="22" width="16" height="12" rx="1.5" fill="#fff"/><rect x="23.5" y="19" width="7" height="4" fill="none" stroke="#fff" stroke-width="1.6"/></svg>

<div class="services-more btn-outline abs">More</div>

<h2 class="vision-title abs">OUR VISION AND<br>MISSION</h2>
<div class="vision-rule abs"></div>
<p class="vision-text abs">Through the commitment of our employees and innovative engineering, we provide highly-reliable flexible circuits, heaters, sensors, instruments, integrated products and services that maximize our customers' competitive advantag</p>
<div class="photo-back abs" role="img" aria-label="Glowing light bulb on a dark background"></div>
<div class="photo-front abs" role="img" aria-label="Portrait of a smiling businessman in a suit"></div>

<h2 class="clients-title abs center">HAPPY CLIENTS</h2>
<div class="clients-rule abs"></div>
<svg class="quote-mark abs" viewBox="0 0 40 40"><circle cx="20" cy="20" r="18" fill="none" stroke="#0a9ad6" stroke-width="2"/><path d="M13 24v-4c0-3 2-5 4-5v2c-1 0-2 1-2 3h2v4zM21 24v-4c0-3 2-5 4-5v2c-1 0-2 1-2 3h2v4z" fill="#0d3a7d"/></svg>
<p class="clients-text abs center">Lantern Advisory has been governed by its core values. They shape the culture and<br>define the character of our company. They guide how we behave and make decisions.</p>
<div class="by abs center">by</div>
<div class="client-name abs center">Manager Dana</div>
<div class="avatar abs" role="img" aria-label="Client portrait"></div>

<section class="consult abs" role="img" aria-label="Hands typing on a laptop keyboard"></section>
<h3 class="consult-title abs">CONSULTING SERVICE</h3>
<p class="consult-sub abs">We Provide wide range of consulting services &amp; world wide happy clients</p>
<div class="start-btn btn-solid abs">START NOW</div>

<div class="footer-bg abs"></div>
<section class="newsletter abs"></section>
<h3 class="news-title abs center">NEWS LETTER</h3>
<div class="field abs" style="left:242px">Name</div>
<div class="field abs" style="left:482px">Email</div>
<div class="subscribe btn-solid abs">SUBSCRIBE</div>

<footer class="site-footer">
  <div class="brand abs"><span class="mark"></span>Lantern Advisory</div>

  <div class="foot-head abs" style="left:368px">Contact Us</div>
  <svg class="foot-icon abs" style="left:362px;top:3388px" viewBox="0 0 16 16"><path d="M8 1a5 5 0 0 0-5 5c0 4 5 9 5 9s5-5 5-9a5 5 0 0 0-5-5zm0 7a2 2 0 1 1 0-4 2 2 0 0 1 0 4z" fill="#fff"/></svg>
  <div class="foot-line abs" style="left:395px;top:3380px">250 Harbor Lane<br>Suite 12<br>Brookfield, ST 00000</div>
  <svg class="foot-icon abs" style="left:362px;top:3463px" viewBox="0 0 16 16"><path d="M4 1l3 3-2 2c1 2 3 4 5 5l2-2 3 3-2 3C7 15 1 9 1 3z" fill="#fff"/></svg>
  <div class="foot-line abs" style="left:395px;top:3460px">+1 (555) 010 2468</div>
  <svg class="foot-icon abs" style="left:362px;top:3502px" viewBox="0 0 16 16"><rect x="1.5" y="3.5" width="13" height="9" fill="none" stroke="#fff" stroke-width="1.4"/><path d="M1.5 3.5l6.5 5 6.5-5" fill="none" stroke="#fff" stroke-width="1.4"/></svg>
  <div class="foot-line abs" style="left:398px;top:3499px">info@lanternadvisory.example</div>

  <div class="foot-head abs" style="left:698px">Quick Links</div>
  <div class="foot-links abs">COMPANY<br>SERVICES<br>SOLUTION<br>RESOURCES<br>CAREER<br>CONTACT US</div>

  <div class="foot-head abs" style="left:940px">Follow Us On</div>
  <div class="social-dot abs" style="left:940px;top:3388px"></div>
  <div class="foot-line abs" style="left:972px;top:3383px">Pagefeed</div>
  <div class="social-dot abs" style="left:940px;top:3431px"></div>
  <div class="foot-line abs" style="left:972px;top:3426px">Worknet</div>
  <div class="social-dot abs" style="left:940px;top:3475px"></div>
  <div class="foot-line abs" style="left:972px;top:3470px">Chirpline</div>

  <div class="copyright abs center">© <b>LANTERN ADVISORY</b> -2016.All Rights Reserved.</div>
</footer>

</body>
</html>
```